依頼詳細
シンプルなデザイン(白・黒)を基調としたデザインをお願いたします。
洗練された雰囲気のあるデザインが希望です。

縦・横それぞれ候補頂けますと幸いです。
記載項目
表面
株式会社ルカ
東京都柊野町14-57-215
TEL:03-5872-1946
FAX:03-5872-1953
HANDY:080-7259-8421
Mail:tani@ruka-example.jp

裏面
ロゴ+何か(会社HPに飛ぶHPでもいいです)
※ロゴだけでもカッコよければそれでもいいかと思ってます。
希望イメージ
希望する色
無彩色系
納品ファイル
• 高解像度JPG (.jpg)
補足説明
従来の縦型のデザインを送ります。
裏面は黒バックにロゴのみでした。

デザインが気に入りました。

この度は、お忙しい中ご提案頂きまして誠にありがとうございました。
また何かありましたら、お付き合いの程よろしくお願い申し上げます。

```html
<!DOCTYPE html>
<html lang="ja">
<head>
<meta charset="UTF-8">
<title>株式会社ルカ 名刺</title>
<link rel="stylesheet" href="https://fonts.googleapis.com/css2?family=Noto+Sans+JP:wght@400;500;700&family=Noto+Serif:ital@1&display=swap">
<style>
  :root {
    --canvas: #ffffff;
    --card-front: #ffffff;
    --card-back: #3a3939;
    --ink: #1f1f1f;
    --ink-soft: #444444;
    --paper-text: #ffffff;
    --shadow: rgba(0, 0, 0, 0.28);
  }
  * { margin: 0; padding: 0; box-sizing: border-box; }
  html, body {
    width: 841px; height: 1200px; overflow: hidden;
    background: var(--canvas);
    font-family: "Noto Sans JP", sans-serif;
    color: var(--ink);
  }
  .sheet { position: relative; width: 841px; height: 1200px; }

  .card {
    position: absolute; left: 78px; width: 692px; height: 420px;
    box-shadow: 0 4px 14px var(--shadow);
  }
  .card--front { top: 84px; background: var(--card-front); }
  .card--back { top: 672px; background: var(--card-back); }

  .title { position: absolute; left: 20px; top: 100px; font-size: 16px; font-weight: 500; }
  .name { position: absolute; left: 20px; top: 122px; font-size: 36px; font-weight: 700; letter-spacing: 2px; }
  .name-roman {
    position: absolute; left: 268px; top: 140px;
    font-family: "Noto Serif", serif; font-style: italic; font-size: 19px;
  }
  .mobile { position: absolute; left: 20px; top: 190px; display: flex; align-items: center; gap: 12px; font-size: 19px; }
  .mobile svg { width: 18px; height: 26px; }

  .company { position: absolute; left: 20px; top: 268px; font-size: 27px; font-weight: 700; }
  .contact { position: absolute; left: 20px; top: 320px; font-size: 15px; line-height: 28px; color: var(--ink-soft); }
  .contact span + span { margin-left: 28px; }

  .brand {
    position: absolute; display: flex; align-items: center; gap: 12px;
    font-weight: 700; letter-spacing: 4px;
  }
  .brand__mark { border: 3px solid currentColor; }
  .brand--front { left: 530px; top: 282px; font-size: 38px; color: var(--ink); }
  .brand--front .brand__mark { width: 30px; height: 30px; }
  .brand--back { left: 0; right: 0; top: 140px; justify-content: center; font-size: 58px; color: var(--paper-text); }
  .brand--back .brand__mark { width: 44px; height: 44px; }

  .url {
    position: absolute; left: 0; right: 0; top: 304px; text-align: center;
    font-size: 25px; color: var(--paper-text); letter-spacing: 0.5px;
  }
</style>
</head>
<body>
<main class="sheet">
  <section class="card card--front" aria-label="名刺 表面">
    <p class="title">代表取締役</p>
    <h1 class="name">谷 奏太</h1>
    <p class="name-roman">Sota Tani</p>
    <p class="mobile">
      <svg viewBox="0 0 18 26" aria-hidden="true">
        <rect x="1.5" y="1.5" width="15" height="23" rx="2.5" fill="none" stroke="currentColor" stroke-width="2"/>
        <line x1="7" y1="21" x2="11" y2="21" stroke="currentColor" stroke-width="2"/>
      </svg>
      080-7259-8421
    </p>
    <h2 class="company">株式会社ルカ</h2>
    <div class="contact">
      <p>〒150-0042 東京都柊野町14-57-215</p>
      <p><span>Tel. 03-5872-1946</span><span>Fax. 03-5872-1953</span></p>
      <p>E-mail. tani@ruka-example.jp</p>
    </div>
    <div class="brand brand--front"><span class="brand__mark"></span>ルカ</div>
  </section>

  <section class="card card--back" aria-label="名刺 裏面">
    <div class="brand brand--back"><span class="brand__mark"></span>ルカ</div>
    <p class="url">https://www.ruka-example.jp</p>
  </section>
</main>
</body>
</html>
```